Start Up Incubator requires a cool, chic website matching logo theme, CODING + DESIGN

Please see the attached brief file,

This project is to code and design, please DO NOT waste both your and my time by submitting off the rack copy/paste designs without reading the brief or looking at our logo, brand feel and image.

Thank you

Target Market(s)

Male and Female
18-40 Years of Age
Varying levels of business experience
Creative
Social Networker
Technologically Savvy

Requirements
Must have
• Color and feel as per logo manual

```html
<!DOCTYPE html>
<html lang="en">
<head>
<meta charset="utf-8">
<title>Hatchway Idea Hub</title>
<link href="https://fonts.googleapis.com/css2?family=Montserrat:wght@400;500;600&family=Mulish:wght@400;600;700&display=swap" rel="stylesheet">
<style>
:root{
  --yellow:#f5b400;
  --dark:#343434;
  --ink:#2b2b2b;
  --grey:#6d6d6d;
  --line:#dcdcdc;
  --white:#ffffff;
}
*{margin:0;padding:0;box-sizing:border-box}
html,body{width:1200px;height:3403px;overflow:hidden;background:var(--white)}
body{position:relative;font-family:"Mulish",Arial,sans-serif;color:var(--ink)}
.abs{position:absolute}
.band{position:absolute;left:0;width:1200px}
h2,.heading{font-family:"Montserrat",Arial,sans-serif;font-weight:500;letter-spacing:1px}
.section-title{position:absolute;left:0;width:1200px;text-align:center;font-size:28px}
.para{position:absolute;left:75px;width:1050px;text-align:center;font-size:13.5px;line-height:23px;color:var(--grey)}
.btn{position:absolute;display:flex;align-items:center;justify-content:center;font-family:"Montserrat",Arial,sans-serif;font-size:12px;font-weight:500;color:var(--white);letter-spacing:.5px}
.btn-yellow{background:var(--yellow)}
.btn-dark{background:var(--dark)}
.photo{position:absolute}

/* header */
.brand{left:73px;top:30px;font-family:"Montserrat",Arial,sans-serif;font-weight:600;font-size:34px;color:var(--yellow);letter-spacing:2px}
.lang{right:73px;top:26px;font-size:12px;color:var(--grey)}
.lang b{color:var(--ink);font-weight:600}
.nav{top:108px;right:60px;display:flex;font-family:"Montserrat",Arial,sans-serif;font-size:11.5px;color:var(--white)}
.nav span{padding:0 24px}

/* hero */
.hero-copy{right:140px;top:200px;width:380px;text-align:center;color:var(--white);font-family:"Montserrat",Arial,sans-serif}
.hero-copy .name{font-size:44px;color:var(--yellow);font-weight:500;letter-spacing:2px}
.hero-copy .sub{font-size:21px;letter-spacing:1px;margin-top:2px}
.hero-copy .big{font-size:58px;letter-spacing:9px;margin-top:10px;line-height:62px}
.hero-copy .mid{font-size:28px;letter-spacing:1px;line-height:32px}
.hero-copy .mid2{font-size:38px;letter-spacing:1px;line-height:44px}
.dots{left:576px;top:530px;display:flex;gap:5px}
.dots i{width:9px;height:9px;border-radius:50%;background:var(--white)}
.dots i:first-child{background:var(--yellow)}

/* product */
.product{position:absolute;top:980px;width:245px}
.product .photo{position:relative;width:245px;height:147px}
.product h3{font-family:"Montserrat",Arial,sans-serif;font-weight:500;font-size:16px;color:var(--yellow);margin-top:24px}
.product p{font-size:11.5px;line-height:17px;color:#d6d6d6;margin-top:6px}
.product .more{font-size:10.5px;color:var(--yellow);margin-top:14px;display:block}

/* feeds */
.feed{position:absolute;top:2284px;width:331px;height:329px;border:1px solid var(--line);background:var(--white)}
.feed-head{height:41px;background:var(--yellow);font-family:"Montserrat",Arial,sans-serif;font-size:15px;font-weight:500;color:var(--ink);padding:12px 14px}
.feed-item{margin:14px 30px 0 14px;font-size:11.5px;line-height:17px;color:var(--grey);padding-bottom:10px;border-bottom:1px solid #eee}
.feed-item a{color:var(--yellow);text-decoration:none}
.feed-item small{display:block;font-size:10px;color:var(--yellow);margin-top:2px}
.scroll{position:absolute;right:14px;top:58px;width:7px;height:30px;background:var(--dark)}
.gallery-grid{display:grid;grid-template-columns:repeat(3,94px);gap:11px;padding:14px}
.gallery-grid div{height:76px}

/* newsletter / contact */
.field{position:absolute;background:var(--white);font-size:12px;color:#777;padding:0 16px;display:flex;align-items:center;letter-spacing:.5px}
.foot-col{position:absolute;top:3062px;font-size:11px;line-height:26px;color:var(--ink)}
.foot-col h4{font-family:"Montserrat",Arial,sans-serif;font-weight:500;font-size:14px;margin-bottom:6px}
.social{display:flex;align-items:center;gap:10px;height:35px}
.social i{width:18px;height:18px;border-radius:50%;background:var(--dark);display:block}
.copy{left:794px;top:3344px;font-size:10px;line-height:16px;color:var(--ink)}
</style>
</head>
<body>

<!-- header -->
<div class="abs brand">HATCHWAY</div>
<div class="abs lang">GERMAN / <b>ENGLISH</b></div>
<svg class="band" style="top:88px" width="1200" height="60" viewBox="0 0 1200 60">
  <polygon points="0,22 1200,0 1200,58 0,58" fill="var(--yellow)"/>
</svg>
<div class="abs nav"><span>HOME</span><span>ABOUT US</span><span>PRODUCT</span><span>CASE STUDIES</span><span>DOWNLOADS</span><span>MEDIA GALLERY</span><span>CONTACT US</span></div>

<!-- hero -->
<div class="photo" role="img" aria-label="Young entrepreneur thinking in front of a chalkboard sketched with business icons" style="left:0;top:147px;width:1200px;height:409px;background:linear-gradient(90deg,#6b6b6b 0%,#4a4a4a 35%,#2a2a2a 65%,#1f1f1f 100%)"></div>
<div class="abs hero-copy">
  <div class="name">HATCHWAY</div>
  <div class="sub">IDEA HUB</div>
  <div class="big">IMAGINE</div>
  <div class="mid">RUNNING A BUSINESS</div>
  <div class="mid2">WITH NO RENT..</div>
</div>
<div class="abs dots"><i></i><i></i><i></i><i></i></div>

<!-- welcome -->
<h2 class="section-title" style="top:588px;color:var(--ink)">WELCOME TO OUR WEBSITE</h2>
<p class="para" style="top:640px">Aliquam molestie, mi et imperdiet euismod, dui purus auctor tellus, et interdum lacus lectus et ante. Sed accumsan sollicitudin sapien, sit amet adipiscing turpis gravida ac. In congue, neque ac lobortis volutpat, libero mauris varius mi, vitae suscipit ipsum ligula vitae risus. Duis aliquam nibh a dui iaculis viverra id a velit. Vivamus egestas risus in magna varius commodo. Sed semper viverra egestas. Etiam pretium porttitor lectus, vel ornare neque porta volutpat. Aenean a nibh eget turpis vehicula tempus ac sed massa. Vestibulum dolor nulla, ultrices ac tincidunt sed, laoreet non est. Suspendisse lobortis turpis in odio blandit ac interdum lorem euismod. Etiam risus massa, vulputate eu pellentesque et, consectetur a neque.</p>
<div class="btn btn-yellow" style="left:532px;top:782px;width:137px;height:48px">LEARN MORE &rsaquo;&rsaquo;</div>

<!-- product offering -->
<svg class="band" style="top:850px" width="1200" height="450" viewBox="0 0 1200 450">
  <polygon points="0,46 1200,0 1200,450 0,450" fill="var(--dark)"/>
</svg>
<h2 class="section-title" style="top:918px;color:var(--yellow)">PRODUCT OFFERING</h2>
<div class="abs" style="left:73px;top:938px;width:370px;height:1px;background:#555"></div>
<div class="abs" style="left:757px;top:938px;width:370px;height:1px;background:#555"></div>

<div class="product" style="left:73px"><div class="photo" role="img" aria-label="Hands joining puzzle pieces" style="background:linear-gradient(135deg,#c9d4e0,#7b8ea6)"></div><h3>PRODUCT HEADING</h3><p>Aliquam molestie, mi et imperdietuismod, dui purus auctor tellus, et interdum lacus lectus et ante...</p><span class="more">LEARN MORE &rsaquo;&rsaquo;</span></div>
<div class="product" style="left:342px"><div class="photo" role="img" aria-label="Hand touching glowing digital icons" style="background:linear-gradient(135deg,#e6e6e6,#8e8e8e)"></div><h3>PRODUCT HEADING</h3><p>Aliquam molestie, mi et imperdietuismod, dui purus auctor tellus, et interdum lacus lectus et ante...</p><span class="more">LEARN MORE &rsaquo;&rsaquo;</span></div>
<div class="product" style="left:612px"><div class="photo" role="img" aria-label="Businessman stacking team figures into a pyramid" style="background:linear-gradient(135deg,#6d87b3,#2f4a78)"></div><h3>PRODUCT HEADING</h3><p>Aliquam molestie, mi et imperdietuismod, dui purus auctor tellus, et interdum lacus lectus et ante...</p><span class="more">LEARN MORE &rsaquo;&rsaquo;</span></div>
<div class="product" style="left:882px"><div class="photo" role="img" aria-label="Hand reaching toward a glowing network diagram" style="background:linear-gradient(135deg,#3d5a80,#16233a)"></div><h3>PRODUCT HEADING</h3><p>Aliquam molestie, mi et imperdietuismod, dui purus auctor tellus, et interdum lacus lectus et ante...</p><span class="more">LEARN MORE &rsaquo;&rsaquo;</span></div>

<!-- case studies -->
<svg class="band" style="top:1296px" width="1200" height="340" viewBox="0 0 1200 340" role="img" aria-label="Yellow tinted office background">
  <defs><linearGradient id="caseTint" x1="0" y1="0" x2="1" y2="1"><stop offset="0" stop-color="#f7be16"/><stop offset="1" stop-color="#f3b000"/></linearGradient></defs>
  <polygon points="0,0 1200,0 1200,334 0,274" fill="url(#caseTint)"/>
</svg>
<h2 class="section-title" style="top:1360px;color:var(--ink)">CASE STUDIES</h2>
<p class="para" style="top:1420px;color:#fff3d0">Aliquam molestie, mi et imperdiet euismod, dui purus auctor tellus, et interdum lacus lectus et ante. Sed accumsan sollicitudin sapien, sit amet adipiscing turpis gravida ac. In congue, neque ac lobortis volutpat, libero mauris varius mi, vitae suscipit ipsum ligula vitae risus. Duis aliquam nibh a dui iaculis viverra id a velit. Vivamus egestas risus in magna varius commodo. Sed semper viverra egestas.</p>
<div class="btn btn-dark" style="left:532px;top:1515px;width:137px;height:50px">LEARN MORE &rsaquo;&rsaquo;</div>

<!-- media gallery -->
<h2 class="section-title" style="top:1656px;color:var(--ink)">MEDIA GALLERY</h2>
<svg class="abs" style="left:48px;top:1768px" width="14" height="24" viewBox="0 0 14 24"><polyline points="12,2 2,12 12,22" fill="none" stroke="var(--ink)" stroke-width="2.5"/></svg>
<svg class="abs" style="left:1138px;top:1768px" width="14" height="24" viewBox="0 0 14 24"><polyline points="2,2 12,12 2,22" fill="none" stroke="var(--ink)" stroke-width="2.5"/></svg>
<div class="photo" role="img" aria-label="Businessman holding a tablet" style="left:73px;top:1712px;width:245px;height:136px;background:linear-gradient(135deg,#5a5a5a,#1e1e1e)"></div>
<div class="photo" role="img" aria-label="Team of colleagues in an office" style="left:342px;top:1712px;width:245px;height:136px;background:linear-gradient(135deg,#e9e3dc,#a69a8e)"></div>
<div class="photo" role="img" aria-label="Colleagues discussing at a laptop" style="left:612px;top:1712px;width:245px;height:136px;background:linear-gradient(135deg,#d6dde5,#7b8c9c)"></div>
<div class="photo" role="img" aria-label="Business meeting around a table" style="left:882px;top:1712px;width:245px;height:136px;background:linear-gradient(135deg,#c9d7e6,#6a86a6)"></div>

<!-- downloads -->
<svg class="band" style="top:1905px" width="1200" height="346" viewBox="0 0 1200 346" role="img" aria-label="Dark background of a person with floating network icons">
  <defs><linearGradient id="dlTint" x1="0" y1="0" x2="1" y2="0"><stop offset="0" stop-color="#4a4d54"/><stop offset=".5" stop-color="#3a3d44"/><stop offset="1" stop-color="#4a4d54"/></linearGradient></defs>
  <polygon points="0,0 1200,45 1200,346 0,346" fill="url(#dlTint)"/>
</svg>
<h2 class="section-title" style="top:1986px;color:var(--yellow)">DOWNLOADS</h2>
<p class="para" style="top:2035px;color:#e6e6e6">Aliquam molestie, mi et imperdiet euismod, dui purus auctor tellus, et interdum lacus lectus et ante. Sed accumsan sollicitudin sapien, sit amet adipiscing turpis gravida ac. In congue, neque ac lobortis volutpat, libero mauris varius mi, vitae suscipit ipsum ligula vitae risus. Duis aliquam nibh a dui iaculis viverra id a velit. Vivamus egestas risus in magna varius commodo. Sed semper viverra egestas.</p>
<div class="btn btn-yellow" style="left:510px;top:2141px;width:180px;height:50px">DOWNLOAD NOW</div>

<!-- feeds -->
<div class="feed" style="left:73px">
  <div class="feed-head">CIRCLEBOOK FEEDS</div><span class="scroll"></span>
  <div class="feed-item">Aliquam molestie, mi et imperdiet euismod, dui purus auctor tellus, et interdum lacus lectus et ante...<small>2 days ago &nbsp;|&nbsp; Like</small></div>
  <div class="feed-item">Aliquam molestie, mi et imperdiet euismod, dui purus auctor tellus, et interdum lacus lectus et ante...<small>2 days ago &nbsp;|&nbsp; Like</small></div>
  <div class="feed-item" style="border:0">Aliquam molestie, mi et imperdiet euismod, dui purus auctor tellus, et interdum lacus lectus et ante...<small>2 days ago &nbsp;|&nbsp; Like</small></div>
</div>
<div class="feed" style="left:433px">
  <div class="feed-head">CHIRPER FEEDS</div><span class="scroll"></span>
  <div class="feed-item">Aliquam molestie, mi et imperdiet euismod, dui purus auctor tellus. <a>http://hw-lnk.io</a> et interdum lacus lectus et ante...<small>2 days ago &nbsp;|&nbsp; Reshares</small></div>
  <div class="feed-item">Aliquam molestie, mi et imperdiet euismod, dui purus auctor tellus. <a>http://hw-lnk.io</a> et interdum lacus lectus et ante...<small>2 days ago &nbsp;|&nbsp; Reshares</small></div>
  <div class="feed-item" style="border:0">Aliquam molestie, mi et imperdiet euismod, dui purus auctor tellus. <a>http://hw-lnk.io</a> et interdum lacus lectus et ante...<small>2 days ago &nbsp;|&nbsp; Reshares</small></div>
</div>
<div class="feed" style="left:792px">
  <div class="feed-head">SNAPGRAM FEEDS</div>
  <div class="gallery-grid">
    <div role="img" aria-label="Team meeting photo" style="background:linear-gradient(135deg,#cfd8e2,#7d8da0)"></div>
    <div role="img" aria-label="Light bulb idea photo" style="background:linear-gradient(135deg,#f3e3b4,#c99b3a)"></div>
    <div role="img" aria-label="Business presentation photo" style="background:linear-gradient(135deg,#4b5668,#1e2430)"></div>
    <div role="img" aria-label="Gears in hands photo" style="background:linear-gradient(135deg,#a9b5c0,#5e6c7a)"></div>
    <div role="img" aria-label="Group of professionals photo" style="background:linear-gradient(135deg,#b9b3ab,#5e5851)"></div>
    <div role="img" aria-label="Growing plant photo" style="background:linear-gradient(135deg,#d9e6c8,#6f8f4e)"></div>
  </div>
</div>

<!-- newsletter -->
<svg class="band" style="top:2642px" width="1200" height="380" viewBox="0 0 1200 380">
  <polygon points="0,53 1200,0 1200,374 0,329" fill="var(--dark)"/>
</svg>
<h2 class="section-title" style="top:2722px;color:var(--yellow)">NEWSLETTER SIGN UP</h2>
<p class="para" style="top:2772px;color:#e6e6e6">Aliquam molestie, mi et imperdiet euismod, dui purus auctor tellus, et interdum lacus lectus et ante. Sed accumsan sollicitudin sapien, sit amet adipiscing turpis gravida ac. In congue, neque ac lobortis volutpat, libero mauris varius mi, vitae suscipit ipsum ligula vitae risus. Duis aliquam nibh a dui iaculis viverra id a velit. Vivamus egestas risus in magna varius commodo. Sed semper viverra egestas.</p>
<div class="field" style="left:254px;top:2880px;width:488px;height:48px">ENTER EMAIL ADDRESS</div>
<div class="btn btn-yellow" style="left:767px;top:2880px;width:179px;height:48px">SIGN UP NOW</div>

<!-- contact footer -->
<svg class="band" style="top:2971px" width="1200" height="432" viewBox="0 0 1200 432">
  <polygon points="0,0 1200,45 1200,432 0,432" fill="var(--yellow)"/>
  <polygon points="0,0 1200,45 1200,0" fill="var(--dark)"/>
</svg>
<h2 class="abs heading" style="left:73px;top:3038px;font-size:28px;color:var(--ink)">CONTACT US / LEAD GENERATION</h2>
<div class="field" style="left:73px;top:3100px;width:292px;height:48px">ENTER NAME</div>
<div class="field" style="left:383px;top:3100px;width:293px;height:48px">ENTER EMAIL</div>
<div class="field" style="left:73px;top:3164px;width:292px;height:48px">TELEPHONE NO.</div>
<div class="field" style="left:383px;top:3164px;width:293px;height:48px">PI INFORMATION
  <svg style="position:absolute;right:14px;top:21px" width="14" height="8" viewBox="0 0 14 8"><polygon points="0,0 14,0 7,8" fill="var(--grey)"/></svg></div>
<div class="field" style="left:73px;top:3225px;width:603px;height:91px;align-items:flex-start;padding-top:14px">MESSAGE</div>
<div class="btn btn-dark" style="left:567px;top:3330px;width:109px;height:45px">SEND</div>

<div class="foot-col" style="left:794px">
  <h4>NAVIGATION</h4>
  HOME<br>ABOUT US<br>PRODUCT OFFERING<br>CASE STUDIES<br>DOWNLOADS<br>MEDIA GALLERY<br>CONTACT US
</div>
<div class="foot-col" style="left:973px">
  <h4>CONNECT US</h4>
  <div class="social"><i></i>CIRCLEBOOK</div>
  <div class="social"><i></i>CHIRPER</div>
  <div class="social"><i></i>SNAPGRAM</div>
</div>
<div class="abs copy">COPYRIGHT &copy; 2014. HATCHWAY . ALL RIGHT RESERVED<br>PRIVACY POLICY</div>

</body>
</html>
```